Dune Air & Plus business card

I need an awesome, double-sided business card designed with our new logo. I would like the one side black with the colored logo, and the back side is all yours. I'd like to see horizontal and vertical layouts. Get creative! Thank you.

Target Market(s)

HVAC, Heating and Cooling in Phoenix, AZ

Industry/Entity Type

HVAC

Contact Information for Business Card

We need our new logo on the card. Tom Harker, (623) 555-0142, tom@trydunesair.com, www.trydunesair.com, ROC 514273

```html
<!DOCTYPE html>
<html lang="en">
<head>
<meta charset="utf-8">
<title>Dune Air &amp; Plus business card</title>
<link href="https://fonts.googleapis.com/css2?family=Montserrat:wght@400;500;700;800&display=swap" rel="stylesheet">
<style>
  :root {
    --backdrop: #3b3b3b;
    --card: #161616;
    --blue: #2a7fd6;
    --blue-edge: #1e78e0;
    --orange: #f07a1e;
    --white: #f2f2f2;
    --grey-hi: #8a8a8a;
    --grey-mid: #454545;
  }
  * { box-sizing: border-box; margin: 0; padding: 0; }
  html, body {
    width: 1200px; height: 801px; overflow: hidden;
    background: var(--backdrop);
    font-family: "Montserrat", sans-serif;
  }
  .stage { position: relative; width: 1200px; height: 801px; }
  .card {
    position: absolute; top: 250px;
    width: 525px; height: 300px;
    background: var(--card);
    border-bottom: 3px solid var(--blue-edge);
    overflow: hidden;
  }
  .card-front { left: 50px; }
  .card-back { left: 625px; }

  .brand { display: flex; align-items: center; gap: 8px; }
  .brand-dot { width: 14px; height: 14px; border-radius: 50%; background: var(--orange); flex: none; }
  .brand-name {
    font-weight: 800; font-size: 17px; letter-spacing: 0.5px;
    color: var(--blue); text-transform: uppercase; white-space: nowrap;
  }

  /* front */
  .front-brand { position: absolute; left: 34px; top: 110px; }
  .identity { position: absolute; right: 34px; top: 34px; text-align: right; }
  .identity-name {
    font-weight: 700; font-size: 19px; color: var(--blue);
    letter-spacing: 0.5px; text-transform: uppercase;
  }
  .identity-licence { font-weight: 400; font-size: 12px; color: var(--white); margin-top: 2px; }
  .rule { position: absolute; height: 1px; background: var(--blue); }
  .rule-top { left: 250px; right: 30px; top: 88px; }
  .rule-bottom { left: 200px; right: 0; top: 198px; }
  .contacts { position: absolute; left: 206px; top: 212px; list-style: none; }
  .contacts li {
    display: flex; align-items: center; gap: 8px;
    font-size: 12px; color: var(--white); line-height: 22px;
  }
  .contacts svg { width: 11px; height: 11px; fill: var(--orange); flex: none; }

  /* back */
  .back-artwork {
    position: absolute; left: 0; right: 0; top: 95px; bottom: 0;
    background:
      radial-gradient(ellipse 55% 75% at 58% 62%, var(--grey-hi) 0%, var(--grey-mid) 45%, rgba(22,22,22,0) 78%),
      linear-gradient(180deg, rgba(22,22,22,0) 0%, rgba(40,40,40,0.6) 100%);
  }
  .back-brand {
    position: absolute; right: 34px; top: 40px; gap: 10px;
  }
  .back-brand .brand-name { font-size: 26px; }
  .back-brand .brand-dot { width: 18px; height: 18px; }
</style>
</head>
<body>
<main class="stage">
  <section class="card card-front" aria-label="Card front">
    <div class="brand front-brand">
      <span class="brand-dot"></span>
      <span class="brand-name">Dune Air &amp; Plus</span>
    </div>
    <div class="identity">
      <p class="identity-name">Tom Harker</p>
      <p class="identity-licence">ROC 514273</p>
    </div>
    <div class="rule rule-top"></div>
    <div class="rule rule-bottom"></div>
    <ul class="contacts">
      <li>
        <svg viewBox="0 0 24 24"><path d="M6.6 10.8a15 15 0 0 0 6.6 6.6l2.2-2.2a1 1 0 0 1 1-.25 11 11 0 0 0 3.6.6 1 1 0 0 1 1 1V20a1 1 0 0 1-1 1A17 17 0 0 1 3 4a1 1 0 0 1 1-1h3.5a1 1 0 0 1 1 1c0 1.25.2 2.45.6 3.6a1 1 0 0 1-.25 1z"/></svg>
        (623) 555-0142
      </li>
      <li>
        <svg viewBox="0 0 24 24"><path d="M2 5h20v14H2zm2 2v.5l8 5 8-5V7l-8 5z"/></svg>
        tom@trydunesair.com
      </li>
      <li>
        <svg viewBox="0 0 24 24"><circle cx="12" cy="12" r="10"/></svg>
        www.trydunesair.com
      </li>
    </ul>
  </section>

  <section class="card card-back" aria-label="Card back">
    <div class="back-artwork" role="img" aria-label="Embossed grey illustration of a house with garage doors, a tree and a setting sun"></div>
    <div class="brand back-brand">
      <span class="brand-dot"></span>
      <span class="brand-name">Dune Air &amp; Plus</span>
    </div>
  </section>
</main>
</body>
</html>
```